Need posters that inspire entrepreneurs

I want to create beautiful, inspiring wall art. I'm looking for a designer to create an awesome sample (note this sample is not for real use). The winning design will form the foundation of our art "style" so there will be LOTS of ongoing work for the winning designer.

It's your challenge to create a style that is clean, inspiring and timeless, and possibly can be adapted to different colour palettes.

Looking for a perfect execution of words, image and design.

The attached example shows one idea. It should serve as an idea only.

Format of the images should be either rectangular or square. Exact size is preferably UK A4 (US letter) or max A3. Assume that a display would consist of a 4 x 4 image grid so size needs to allow for that in a small to medium size office.

The quotes I want in the 3 samples (each in an individual poster - not combined in 1 poster). Each quote should have it's own, the reason for three is to prove the design work on more than one quote. The quotes are:

1) Failure is the condiment that gives success its flavor.
– Wendell Ruskin

2) Whether you think you can or think you can’t, you’re right.
– Milo Dagwell

3) Ever tried. Ever failed. No matter. Try Again. Fail again. Fail better.
– Oswin Tarrant

Each design should include the image of the person and the quote + any design elements you consider relevant. You should find relevant images of the individuals being quoted. The final images will not be published or used commercially in any way.

Font styles to use
Serif
Sans Serif

Colors

Designer to choose colors to be used in the design.

Requirements
Must have
• Words and headshot image - 1 per poster design.
• Please consider in the design that there will not always be photographs of the person quoted and as such the design will need to hold, whether the source is a photo, sketch or something else.
Nice to have
• None, but note that the final image will be printed on a wall mounted board, printed to the edge but not on the edge. The board will have black or white edges so consider in the design.
Should not have
• None

```html
<!DOCTYPE html>
<html lang="en">
<head>
<meta charset="utf-8">
<title>Whether you think you can – Milo Dagwell</title>
<link rel="stylesheet" href="https://fonts.googleapis.com/css2?family=Josefin+Sans:wght@400&family=Pirata+One&display=swap">
<style>
  :root {
    --bg-top: #c4afa3;
    --bg-mid: #a48878;
    --bg-bottom: #6d5142;
    --band-light: #f6eeec;
    --ink: #1c1714;
    --ink-faded: #2e2520;
    --cream: #f1e6d8;
    --figure-dark: #1b1714;
    --figure-mid: #3a322d;
  }
  * { margin: 0; padding: 0; box-sizing: border-box; }
  html, body { width: 1200px; height: 1200px; overflow: hidden; }
  .poster {
    position: relative;
    width: 1200px;
    height: 1200px;
    overflow: hidden;
    background: linear-gradient(180deg, var(--bg-top) 0%, var(--bg-mid) 55%, var(--bg-bottom) 100%);
  }
  .brush-band {
    position: absolute;
    left: -40px;
    top: 60px;
    width: 1300px;
    height: 600px;
    background: radial-gradient(ellipse 70% 60% at 45% 50%, var(--band-light) 0%, rgba(246,238,236,0.85) 55%, rgba(246,238,236,0) 100%);
  }
  .quote {
    position: absolute;
    left: 100px;
    top: 0;
    font-family: "Josefin Sans", sans-serif;
    font-weight: 400;
    text-transform: uppercase;
    letter-spacing: -2px;
    color: var(--ink);
  }
  .quote-line {
    position: absolute;
    left: 0;
    white-space: nowrap;
    line-height: 1;
    transform: scaleX(0.74);
    transform-origin: left top;
  }
  .quote-line--faded { color: var(--ink-faded); opacity: 0.88; }
  .line-1 { top: 80px;  font-size: 111px; }
  .line-2 { top: 229px; font-size: 131px; }
  .line-3 { top: 376px; font-size: 143px; }
  .line-4 { top: 554px; font-size: 114px; }
  .line-5 { top: 678px; font-size: 114px; }
  .line-6 { top: 832px; font-size: 137px; }
  .attribution {
    position: absolute;
    left: 296px;
    top: 1014px;
    width: 440px;
    text-align: center;
    font-family: "Pirata One", serif;
    font-size: 66px;
    line-height: 1.2;
    color: var(--cream);
    white-space: nowrap;
  }
  .attribution .dash { font-family: "Josefin Sans", sans-serif; font-size: 44px; vertical-align: middle; }
  .portrait {
    position: absolute;
    left: 880px;
    top: 144px;
    width: 320px;
    height: 1056px;
    border-radius: 130px 130px 0 0;
    background: linear-gradient(180deg, var(--figure-mid) 0%, var(--figure-dark) 40%, var(--figure-dark) 100%);
  }
</style>
</head>
<body>
  <main class="poster">
    <div class="brush-band"></div>

    <div class="quote">
      <div class="quote-line quote-line--faded line-1">Whether</div>
      <div class="quote-line line-2">You think</div>
      <div class="quote-line line-3">You can</div>
      <div class="quote-line quote-line--faded line-4">Or think</div>
      <div class="quote-line quote-line--faded line-5">You can’t,</div>
      <div class="quote-line line-6">You’re right.</div>
    </div>

    <p class="attribution"><span class="dash">~</span> Milo Dagwell <span class="dash">~</span></p>

    <div class="portrait" role="img" aria-label="Black and white photograph of Milo Dagwell standing in a dark overcoat and bowler hat"></div>
  </main>
</body>
</html>
```